Design Large Inspirational Artwork with Long Quote

Design a large piece of art with a quote from Marcus Hallwell.

QUOTE
"The thing that's so interesting about being alive is that you're all in. No matter what you do, you're all in. This is gonna kill you, so I think you might as well play the most magnificent game you can while you're waiting. Because, do you have anything better to do? Why not pick the best thing possible that you could do? Because you're more powerful than you think, way more powerful than you think. I mean, God only knows what you are in the final analysis. You're blind to your own weaknesses, but you're also blind to your own strengths. How far could you take that if you stopped wasting time, and if you stopped lying, and if you oriented yourself to the highest possible good that you could conceive of and you committed to that? How much good could you do? Well, I would say: why don't you find out?"

SIZE
A high-resolution print size of 6' wide and 3' tall should provide ample space for both the quote and the accompanying artwork.

TYPOGRAPHY
Choose a bold, clean, and easily readable font for the quote. You could also experiment with different font sizes for certain words or phrases to emphasize their importance within the quote.

COLORS
Since the quote is thought-provoking and reflective, you might want to use a color palette that evokes a sense of introspection and depth. Consider using cool, calming colors like shades of blue, gray, or green. Alternatively, you can use a contrasting color scheme with a light background and dark text to make the quote stand out.

ARTWORK
Select / create / edit background artwork to complement the quote.
While a great design might be minimalistic and/or greyscale, I'd really like to see some full color options. This might be anything from photography or graphics inspired by the ideas in the text, to abstract colors or illustrations that feel like the sentiment expressed.
The art should capture your attention and encourage you to read the text. The art should be visually appealing, both at a distance and up close, regardless of whether the text is read.
Updates

Having trouble confirming the exact print size.

Still looking for printing solution and final size confirmation.

Target Market(s)

Personal, business, office

Industry/Entity Type

None

Font styles to use
Sans Serif
Script

Requirements
Must have
• Entire quote, legible text, modern design, attractive artwork, approx 6ft wide and 3ft tall
Nice to have
• Different font (sizes) for certain words or phrases to emphasize their importance within the quote.

```html
<!DOCTYPE html>
<html lang="en">
<head>
<meta charset="utf-8">
<title>All In — Marcus Hallwell Quote Art</title>
<link rel="stylesheet" href="https://fonts.googleapis.com/css2?family=Crimson+Pro:wght@400;600;700&display=swap">
<style>
  :root {
    --ink-white: #ffffff;
    --banner-text: #123a7a;
    --sea-light: #8fd3e6;
    --sea-mid: #2a8fd0;
    --sky-deep: #1556c4;
    --night-blue: #23239a;
    --sun: #ffffff;
    --shadow: rgba(4, 20, 70, 0.85);
  }
  html, body {
    margin: 0;
    padding: 0;
    width: 1200px;
    height: 602px;
    overflow: hidden;
    background: var(--sky-deep);
  }
  .artwork {
    position: relative;
    width: 1200px;
    height: 602px;
    overflow: hidden;
    font-family: "Crimson Pro", Georgia, serif;
  }
  .backdrop {
    position: absolute;
    inset: 0;
    background:
      radial-gradient(circle at 320px 10px, var(--sun) 0, rgba(255,255,255,0.85) 40px, rgba(180,230,255,0.35) 140px, rgba(120,200,255,0) 300px),
      linear-gradient(180deg, rgba(255,255,255,0) 55%, rgba(210,225,235,0.45) 100%),
      linear-gradient(90deg, var(--sea-light) 0%, var(--sea-mid) 22%, var(--sky-deep) 60%, var(--night-blue) 100%);
  }
  .quote-layer {
    position: absolute;
    inset: 0;
  }
  .quote-layer text {
    fill: var(--ink-white);
    font-family: "Crimson Pro", Georgia, serif;
    font-weight: 400;
  }
  .quote-layer .strong { font-weight: 700; }
  .quote-layer .banner-text { fill: var(--banner-text); font-weight: 600; }
  .quote-layer .mark { font-weight: 700; }
  .frame-line { stroke: var(--ink-white); stroke-width: 4; fill: none; }
  .box-line { stroke: var(--ink-white); stroke-width: 3; fill: none; }
  .icon-line { stroke: var(--ink-white); fill: none; stroke-linecap: round; stroke-linejoin: round; }
  .icon-fill { fill: var(--ink-white); }
</style>
</head>
<body>
<main class="artwork">
  <div class="backdrop" role="img" aria-label="Photograph of a bright sun in a blue sky above a tropical turquoise sea and sandy beach"></div>

  <svg class="quote-layer" width="1200" height="602" viewBox="0 0 1200 602" xmlns="http://www.w3.org/2000/svg">
    <defs>
      <filter id="text-shadow" x="-10%" y="-30%" width="120%" height="160%">
        <feDropShadow dx="2" dy="2" stdDeviation="1.6" flood-color="#04144a" flood-opacity="0.85"/>
      </filter>
    </defs>

    <!-- frame -->
    <g class="quote-frame" filter="url(#text-shadow)">
      <polyline class="frame-line" points="60,41 1143,41 1143,545"/>
      <polyline class="frame-line" points="36,60 36,551 1118,551"/>
      <text class="mark" x="26" y="72" font-size="60">“</text>
      <text class="mark" x="1118" y="584" font-size="60">”</text>
    </g>

    <g class="quote-text" filter="url(#text-shadow)">
      <!-- opening banner -->
      <polygon class="icon-fill" points="66,78 594,78 594,111 66,111 80,94.5"/>
      <text class="banner-text" x="94" y="103" font-size="28" textLength="482" lengthAdjust="spacingAndGlyphs">The thing that's so interesting about being</text>

      <text class="strong" x="585" y="140" font-size="84" textLength="168" lengthAdjust="spacingAndGlyphs">ALIVE</text>

      <rect class="box-line" x="758" y="83" width="106" height="59"/>
      <text x="789" y="107" font-size="19" textLength="44" lengthAdjust="spacingAndGlyphs">is that</text>
      <text x="764" y="127" font-size="19" textLength="94" lengthAdjust="spacingAndGlyphs">you're all in.</text>

      <text x="875" y="100" font-size="27" textLength="156" lengthAdjust="spacingAndGlyphs">This is gonna</text>
      <text class="strong" x="875" y="139" font-size="48" textLength="156" lengthAdjust="spacingAndGlyphs">kill you</text>
      <rect class="icon-fill" x="1036" y="88" width="78" height="52" rx="6" opacity="0.9" role="img" aria-label="Illustration of a handgun"/>

      <text x="84" y="137" font-size="26" textLength="470" lengthAdjust="spacingAndGlyphs">No matter what you do, <tspan class="strong" font-size="30">you're all in.</tspan></text>

      <text x="87" y="170" font-size="28" textLength="1032" lengthAdjust="spacingAndGlyphs">so I think you might as well play the <tspan class="strong">most magnificent game</tspan> you can, while you're waiting</text>

      <text x="83" y="207" font-size="28" textLength="1047" lengthAdjust="spacingAndGlyphs">Because, <tspan class="strong" font-size="30">do you have anything better to do?</tspan> Why not pick <tspan class="strong" font-size="30">the best thing possible</tspan></text>

      <text x="84" y="243" font-size="29" textLength="446" lengthAdjust="spacingAndGlyphs"><tspan class="strong">that you could do?</tspan> Because you're</text>

      <!-- dumbbell -->
      <g class="dumbbell">
        <rect class="icon-line" stroke-width="3" x="541" y="222" width="12" height="32" rx="5"/>
        <rect class="icon-line" stroke-width="3" x="597" y="222" width="12" height="32" rx="5"/>
        <line class="icon-line" stroke-width="3" x1="553" y1="238" x2="597" y2="238"/>
        <rect class="icon-fill" x="563" y="230" width="24" height="16" rx="5"/>
      </g>

      <text class="strong" x="626" y="243" font-size="36" textLength="483" lengthAdjust="spacingAndGlyphs">more powerful than you think,</text>

      <text x="87" y="287" font-size="31" textLength="141" lengthAdjust="spacingAndGlyphs">way more</text>
      <text class="strong" x="240" y="287" font-size="50" textLength="504" lengthAdjust="spacingAndGlyphs">powerful than you think.</text>

      <rect class="box-line" x="759" y="256" width="312" height="54"/>
      <text class="strong" x="766" y="279" font-size="22" textLength="296" lengthAdjust="spacingAndGlyphs">I mean, God only knows what</text>
      <text class="strong" x="766" y="301" font-size="22" textLength="276" lengthAdjust="spacingAndGlyphs">you are in the final analysis.</text>

      <text x="84" y="336" font-size="31" textLength="999" lengthAdjust="spacingAndGlyphs"><tspan class="strong">You're blind to your own weaknesses</tspan>, but you're also blind to your own <tspan class="strong">strengths.</tspan></text>

      <text x="86" y="375" font-size="26" textLength="622" lengthAdjust="spacingAndGlyphs">How far could you take that if you stopped <tspan class="strong" font-size="30">wasting time,</tspan></text>

      <!-- clock -->
      <g class="clock">
        <circle class="icon-line" stroke-width="2.5" cx="731" cy="364" r="18"/>
        <circle class="icon-line" stroke-width="1.5" stroke-dasharray="2 4" cx="731" cy="364" r="14"/>
        <polyline class="icon-line" stroke-width="2.5" points="724,355 738,364 728,372"/>
      </g>

      <text x="761" y="372" font-size="27" textLength="338" lengthAdjust="spacingAndGlyphs">and if you stopped <tspan class="strong">lying</tspan>, and</text>

      <text x="90" y="416" font-size="30" textLength="1007" lengthAdjust="spacingAndGlyphs">if you oriented yourself to the <tspan class="strong" font-size="32">highest possible good</tspan> that you could conceive</text>

      <text x="89" y="456" font-size="30" textLength="888" lengthAdjust="spacingAndGlyphs">of and you committed to that? <tspan class="strong" font-size="31">How much good could you do?</tspan></text>

      <!-- closing line -->
      <circle class="icon-fill" cx="144" cy="493" r="6"/>
      <circle class="icon-fill" cx="163" cy="493" r="6"/>
      <circle class="icon-fill" cx="183" cy="493" r="7.5"/>
      <text x="204" y="507" font-size="46" textLength="735" lengthAdjust="spacingAndGlyphs">Well, I would say: <tspan class="strong">why don't you find out?</tspan></text>

      <!-- magnifier -->
      <g class="magnifier">
        <circle class="icon-line" stroke-width="4" cx="982" cy="493" r="20"/>
        <line class="icon-line" stroke-width="5" x1="996" y1="508" x2="1017" y2="522"/>
      </g>
    </g>
  </svg>
</main>
</body>
</html>
```